Hearthside Pots: A Patient Palate's Companion

Hi, I had a book cover designed on this site, but I want to modify the cover and change the colours. I want to keep the slow cooker and the ingredients on the cover, but I want to simplify it a bit. And, I am open to other ideas. I have attached below a book cover idea I like and I like the colors as well. I want it to be called Hearthside Pots, with the language on the right corner: "Curated For Nearly Effortless Meals That Are Greater Than The Sum Of Their Ingredients" I like the circles idea and my name as the author on the curve.

Target Market(s)

Home Cooks

Colors
00AB8E
00BBA5
67D7C9
C6EFE9
E9F9F6
F0912C
F2A743
F7CA91
FBE8D2
FDF5EE
E54698
E96AAD
F1A4CE
F9D9EA
FCEFF6
6B429C
8869AF
B7A5CE
E3DAEB
F3F0F8

Requirements
Must have
• Please use the colors on the Marigold Table Recipe Book and I like the design, but I do not want it identical. I like the author name (Harold P. Quimby) on the side of the circle on the upper right side of the cover.
Nice to have
• I like the large words "Hearthside Pots"

```html
<!DOCTYPE html>
<html lang="en">
<head>
<meta charset="utf-8">
<title>Hearthside Pots – Cover</title>
<link rel="stylesheet" href="https://fonts.googleapis.com/css2?family=DM+Serif+Display&family=Poppins:wght@400&display=swap">
<style>
  :root {
    --page-bg: #ffffff;
    --teal-deep: #00AB8E;
    --teal: #00BBA5;
    --teal-light: #67D7C9;
    --smoke-deep: #0a8f3c;
    --smoke-mid: #12b25a;
    --orange: #F0912C;
    --amber: #F2A743;
    --peach: #F7CA91;
    --pink: #E54698;
    --plum: #6B429C;
    --circle-dark: #0b2a18;
    --circle-yellow: #ffd21a;
    --pot-black: #1c1310;
    --table-brown: #4a3324;
    --table-deep: #1e140e;
    --title-ink: #2e1a0e;
    --light-ink: #ffffff;
  }
  html, body {
    margin: 0;
    width: 1200px;
    height: 2400px;
    overflow: hidden;
    background: var(--page-bg);
  }
  .book-cover {
    position: absolute;
    left: 100px;
    top: 564px;
    width: 1000px;
    height: 1272px;
    display: block;
  }
  .tagline {
    font-family: "Poppins", sans-serif;
    font-size: 31px;
    fill: var(--light-ink);
  }
  .author-name {
    font-family: "Poppins", sans-serif;
    font-size: 31px;
    letter-spacing: 1px;
    fill: var(--light-ink);
  }
  .title {
    font-family: "DM Serif Display", serif;
    fill: var(--title-ink);
  }
</style>
</head>
<body>
<svg class="book-cover" viewBox="0 0 930 1183" xmlns="http://www.w3.org/2000/svg">
  <defs>
    <radialGradient id="smoke" cx="0.45" cy="0.38" r="0.8">
      <stop offset="0" stop-color="var(--teal)"/>
      <stop offset="0.5" stop-color="var(--smoke-mid)"/>
      <stop offset="1" stop-color="var(--smoke-deep)"/>
    </radialGradient>
    <radialGradient id="pot-scene" cx="0.45" cy="0.35" r="0.75">
      <stop offset="0" stop-color="var(--orange)"/>
      <stop offset="0.18" stop-color="var(--pot-black)"/>
      <stop offset="0.5" stop-color="var(--table-brown)"/>
      <stop offset="1" stop-color="var(--table-deep)"/>
    </radialGradient>
    <linearGradient id="ingredients" x1="0" y1="0" x2="1" y2="0">
      <stop offset="0" stop-color="var(--peach)" stop-opacity="0.35"/>
      <stop offset="0.2" stop-color="var(--peach)" stop-opacity="0"/>
      <stop offset="0.72" stop-color="var(--orange)" stop-opacity="0"/>
      <stop offset="0.85" stop-color="var(--orange)" stop-opacity="0.4"/>
      <stop offset="1" stop-color="var(--amber)" stop-opacity="0.35"/>
    </linearGradient>
    <path id="author-arc" d="M 128 432 A 180 180 0 0 1 370 300"/>
  </defs>

  <rect class="smoke-backdrop" width="930" height="1183" fill="url(#smoke)" role="img" aria-label="Green and teal drifting steam backdrop"/>

  <text class="tagline" x="465" y="108" text-anchor="middle">Curated For Nearly Effortless Meals That Are</text>
  <text class="tagline" x="465" y="148" text-anchor="middle">Greater Than The Sum Of Their Ingredients</text>

  <g class="circle-cluster">
    <circle class="circle circle-teal" cx="111" cy="633" r="145" fill="var(--teal-light)" opacity="0.8"/>
    <circle class="circle circle-dark" cx="594" cy="463" r="142" fill="var(--circle-dark)" opacity="0.85"/>
    <circle class="circle circle-yellow" cx="461" cy="815" r="360" fill="var(--circle-yellow)" opacity="0.9"/>
    <circle class="circle circle-orange" cx="314" cy="463" r="147" fill="var(--orange)" opacity="0.85"/>
    <circle class="circle circle-green" cx="806" cy="623" r="145" fill="var(--teal-deep)" opacity="0.75"/>
  </g>

  <text class="author-name"><textPath href="#author-arc">Harold P. Quimby</textPath></text>

  <text class="title title-top" x="470" y="640" text-anchor="middle" font-size="100">Hearthside</text>
  <text class="title title-bottom" x="470" y="748" text-anchor="middle" font-size="130">Pots</text>

  <g class="pot-scene" role="img" aria-label="Photo: slow cooker pot of carrot stew on a rustic wooden table with bowls, carrots and a loaf of bread">
    <rect x="0" y="790" width="930" height="393" fill="url(#pot-scene)"/>
    <rect x="0" y="790" width="930" height="393" fill="url(#ingredients)"/>
  </g>
</svg>
</body>
</html>
```